New business card for civil engineering company - "Keystone Audit"

We need a business card designed for our new structural engineering company.

The company name is "Keystone Audit" logo files attached.

We would like the following:
* Two-sided card
* Simple design

Information to be placed on the card:
Name - Marcus Dellow
Job Title - Director / Structural Engineer
Credentials - BEng(Hons), CPEng, CMengNZ, IntPE(NZ)
Email - marcus.dellow@keystoneaudit.co.nz
mobile - 0219364058
website - www.keystoneaudit.co.nz

```html
<!DOCTYPE html>
<html lang="en">
<head>
<meta charset="utf-8">
<title>Keystone Audit – Business Card</title>
<link rel="stylesheet" href="https://fonts.googleapis.com/css2?family=Exo+2:wght@300;400;600;700&display=swap">
<style>
  :root {
    --backdrop: #8c8c90;
    --brand-navy: #134670;
    --brand-blue: #2f78b8;
    --card-white: #ffffff;
    --ink-dark: #2b2b2f;
    --ink-grey: #8d9096;
    --name-blue: #2d5d92;
    --link-navy: #0f3c66;
  }
  * { box-sizing: border-box; margin: 0; padding: 0; }
  html, body {
    width: 1200px; height: 913px; overflow: hidden;
    background: var(--backdrop);
    font-family: "Exo 2", sans-serif;
  }
  .canvas { position: relative; width: 1200px; height: 913px; }

  .card {
    position: absolute;
    box-shadow: 0 14px 30px rgba(0,0,0,0.28);
  }

  /* Front side */
  .card-front {
    left: 80px; top: 300px; width: 540px; height: 309px;
    background: var(--brand-navy);
  }
  .brand-lockup {
    position: absolute; left: 56px; bottom: 74px;
  }
  .brand-row { display: flex; align-items: center; gap: 14px; }
  .brand-square {
    width: 26px; height: 26px; background: var(--brand-blue);
  }
  .brand-name {
    color: var(--card-white);
    font-weight: 700; font-size: 38px; letter-spacing: 2px;
    text-transform: uppercase; line-height: 1;
  }
  .brand-tagline {
    margin-top: 10px; margin-left: 40px;
    color: var(--card-white);
    font-weight: 400; font-size: 13px; letter-spacing: 5px;
    text-transform: uppercase;
  }

  /* Back side */
  .card-back {
    left: 720px; top: 186px; width: 309px; height: 540px;
    background: var(--card-white);
  }
  .contact-block { position: absolute; left: 30px; right: 20px; bottom: 48px; }
  .person-name {
    color: var(--name-blue); font-weight: 300; font-size: 30px; line-height: 1.1;
  }
  .person-role {
    margin-top: 4px; color: var(--ink-dark); font-weight: 400; font-size: 15px;
  }
  .person-credentials {
    margin-top: 3px; color: var(--ink-grey); font-weight: 600; font-size: 10.5px;
  }
  .contact-list { list-style: none; margin-top: 24px; }
  .contact-list li {
    color: var(--ink-dark); font-size: 12.5px; font-weight: 400; margin-bottom: 8px;
  }
  .contact-label { color: var(--link-navy); font-weight: 700; margin-right: 6px; }
  .contact-web { color: var(--link-navy); font-weight: 700; font-size: 14px; }
</style>
</head>
<body>
<main class="canvas">
  <section class="card card-front" aria-label="Card front">
    <div class="brand-lockup">
      <div class="brand-row">
        <span class="brand-square"></span>
        <span class="brand-name">Keystone Audit</span>
      </div>
      <div class="brand-tagline">Peer Review Specialists</div>
    </div>
  </section>

  <section class="card card-back" aria-label="Card back">
    <div class="contact-block">
      <h1 class="person-name">Marcus Dellow</h1>
      <p class="person-role">Director / Structural Engineer</p>
      <p class="person-credentials">BEng(Hons), CPEng, CMengNZ, IntPE(NZ)</p>
      <ul class="contact-list">
        <li><span class="contact-label">e:</span>marcus.dellow@keystoneaudit.co.nz</li>
        <li><span class="contact-label">m:</span>0219364058</li>
        <li class="contact-web">www.keystoneaudit.co.nz</li>
      </ul>
    </div>
  </section>
</main>
</body>
</html>
```